Stationery Design Project

We need letterhead and business cards designed for our consulting firm. Color scheme, mostly deep blue (see logo). We are a commercial consulting work out firm, nationwide (large loans, $10MM and up). Visit our website for more info.
Updates

Project Deadline Extended
Reason: Meeting tomorrow morning to make final final decision. Would like this project to stay open to be able to provide feed back and receive final edits and approve. Thank you!!!

Target Market(s)

High end investors

Industry/Entity Type

Business

Requirements
Must have
• Letterhead must have the logo and the address

4817 Larkmoor Avenue, Suite 210, San Diego, CA 92107
Nice to have
• It would be nice to incorporate a watermark of all or some portion of the logo on the letterhead, or at least for the 2nd sheets.

Maybe our phone number: 858.555.0174
and/or webiste: www.tollandridgecap.example
Should not have
• Target users and audience of this will be men so, frilly or whimsical type designs are not preferred.

```html
<!DOCTYPE html>
<html lang="en">
<head>
<meta charset="utf-8">
<title>Tolland Ridge Capital — Stationery</title>
<link href="https://fonts.googleapis.com/css2?family=Cinzel:wght@400;600&family=Crimson+Text:wght@400;600&display=swap" rel="stylesheet">
<style>
  :root {
    --backdrop: #e3e4e6;
    --paper: #ffffff;
    --ink-grey: #5c5e61;
    --watermark: #efefef;
    --brand-blue: #1f4c94;
    --brand-blue-light: #4d78b3;
    --rule-dark: #3b3d40;
    --panel-grey: #8e9297;
    --text-light: #ffffff;
  }
  * { box-sizing: border-box; margin: 0; padding: 0; }
  html, body {
    width: 1200px; height: 1006px; overflow: hidden;
    background: var(--backdrop);
  }
  .stationery { position: relative; width: 1200px; height: 1006px; }

  /* Letterhead */
  .letterhead {
    position: absolute; left: 150px; top: 48px;
    width: 700px; height: 906px;
    background: var(--paper);
    box-shadow: 0 6px 24px rgba(0,0,0,.12);
  }
  .letterhead__brand {
    position: absolute; top: 62px; left: 0; right: 0;
    text-align: center;
    font-family: "Cinzel", serif; font-weight: 600;
    font-size: 30px; letter-spacing: 2px;
    color: var(--ink-grey);
  }
  .letterhead__watermark {
    position: absolute; top: 380px; left: 0; right: 0;
    text-align: center;
    font-family: "Cinzel", serif; font-weight: 600;
    font-size: 64px; line-height: 1.1; letter-spacing: 3px;
    color: var(--watermark);
  }
  .letterhead__address {
    position: absolute; bottom: 92px; left: 0; right: 0;
    text-align: center;
    font-family: "Cinzel", serif; font-weight: 400;
    font-size: 15px; letter-spacing: 1px;
    color: var(--ink-grey);
  }
  .letterhead__bands {
    position: absolute; bottom: 34px; left: 0; right: 0;
  }
  .band-blue { height: 11px; background: var(--brand-blue); }
  .band-gap { height: 5px; }
  .band-dark { height: 5px; background: var(--rule-dark); }

  /* Business card */
  .business-card {
    position: absolute; left: 600px; top: 560px;
    width: 350px; height: 200px;
    background: var(--paper);
    box-shadow: 0 8px 22px rgba(0,0,0,.22);
    overflow: hidden;
  }
  .card__brand {
    position: absolute; top: 52px; left: 0; width: 230px;
    text-align: center;
    font-family: "Cinzel", serif; font-weight: 600;
    font-size: 19px; line-height: 1.2; letter-spacing: 1px;
    color: var(--ink-grey);
  }
  .card__contact {
    position: absolute; right: 0; top: 80px;
    width: 122px; height: 56px;
    background: var(--panel-grey);
    padding: 6px 8px;
    font-family: "Crimson Text", serif; font-size: 7.5px; line-height: 1.35;
    color: var(--text-light);
  }
  .card__person {
    position: absolute; left: 0; top: 136px;
    width: 228px; height: 48px;
    background: linear-gradient(90deg, var(--brand-blue), var(--brand-blue-light));
    padding: 7px 0 0 50px;
    font-family: "Crimson Text", serif; color: var(--text-light);
  }
  .card__name { font-size: 16px; font-weight: 600; line-height: 1.1; }
  .card__role { font-size: 10px; }
</style>
</head>
<body>
<main class="stationery">
  <section class="letterhead">
    <div class="letterhead__brand">Tolland Ridge Capital</div>
    <div class="letterhead__watermark" aria-hidden="true">Tolland Ridge<br>Capital</div>
    <p class="letterhead__address">4817 Larkmoor Avenue, Suite 210, San Diego, CA 92107</p>
    <div class="letterhead__bands">
      <div class="band-blue"></div>
      <div class="band-gap"></div>
      <div class="band-dark"></div>
    </div>
  </section>

  <section class="business-card">
    <div class="card__brand">Tolland Ridge<br>Capital</div>
    <div class="card__contact">
      4817 Larkmoor Avenue, Suite 210,<br>
      San Diego, CA 92107<br>
      T. 858.555.0174 &nbsp;F. 858.555.0190<br>
      E. info@tollandridgecap.example
    </div>
    <div class="card__person">
      <div class="card__name">Marcus Hale</div>
      <div class="card__role">Founder / Owner</div>
    </div>
  </section>
</main>
</body>
</html>
```